Business Card

we need a logo designed for a company that has been in business since 1985
it is called "Varn Hydraulic & Groundworks Repairs Pty Ltd"
We repair Earthmoving machines (big machines used on mine sites)
We also sell parts to suit them and would like the back of the card to show our brands we sell.
This is a new card for out parts manager we need it designed for her to hand out in business meetings to drive more parts sales
Website details
and contact details are essential

Morvel, Plinter & Sharp ridge logos on the back are priorities
Secondary Orient Buildco, Halvstrom

Target Market(s)

This is for the mining industry
Mechanical repairs

Industry/Entity Type

Business

Requirements
Must have
• Company Name: Varn Hydraulic & Groundworks (this logo to be on the front please)
Company message:"Invite us to your next breakdown
Can we make these changable for other staff?
Name: Delia Pranton
Job Title: Parts Manager
Phone: (07) 4916 2087
Fax: (07) 4916 3650
Email: parts@varnhydro.com.au
Address: 2a Tembley Street (PO Box 6475) Mount Isa QLD 4825
www.varnhydro.com.au
Nice to have
• Written on there
New & used parts to suit all types of machinery
Service - Repairs- Overhauls- Labour hire

I would like to get them printed with Printsy so can you please follow there guidelines
http://www.printsyco.com.au/pp/ns/promode/SendFiles.aspx?selectedTab=0?pfid=K47&pf_id=K47&xnav=product-page#FileTypes
Should not have
• Any tooling photos,

```html
<!DOCTYPE html>
<html lang="en">
<head>
<meta charset="utf-8">
<title>Varn Hydraulic &amp; Groundworks – Business Card</title>
<link rel="stylesheet" href="https://fonts.googleapis.com/css2?family=Abril+Fatface&family=Archivo:wght@800&family=Fira+Sans:wght@400;500&family=Playfair+Display:ital,wght@1,900&display=swap">
<style>
  :root {
    --cyan: #2fe4ef;
    --white: #ffffff;
    --ink: #111111;
    --orange: #f7881e;
    --border: #1a1a1a;
  }
  html, body {
    margin: 0;
    padding: 0;
    overflow: hidden;
    background: var(--white);
  }
  .card {
    position: relative;
    width: 1200px;
    height: 687px;
    box-sizing: border-box;
    border: 2px solid var(--border);
    background: linear-gradient(90deg, var(--cyan) 0%, #8ff0f6 45%, var(--white) 100%);
    overflow: hidden;
    color: var(--ink);
  }
  .brand-mark {
    position: absolute;
    left: 70px;
    top: 44px;
    width: 140px;
    height: 140px;
    background: var(--orange);
  }
  .company-name {
    position: absolute;
    left: 279px;
    top: 22px;
    margin: 0;
    font-family: "Abril Fatface", serif;
    font-weight: 400;
    font-size: 56px;
    line-height: 1;
    white-space: nowrap;
  }
  .tagline {
    position: absolute;
    left: 342px;
    top: 84px;
    margin: 0;
    font-family: "Playfair Display", serif;
    font-style: italic;
    font-weight: 900;
    font-size: 29px;
    line-height: 1;
    white-space: nowrap;
  }
  .person-name {
    position: absolute;
    right: 14px;
    top: 106px;
    margin: 0;
    font-family: "Fira Sans", sans-serif;
    font-weight: 500;
    font-size: 40px;
    line-height: 1;
    letter-spacing: -0.5px;
  }
  .person-title {
    position: absolute;
    left: 974px;
    top: 156px;
    margin: 0;
    font-family: "Fira Sans", sans-serif;
    font-weight: 400;
    font-size: 24px;
    line-height: 1;
  }
  .services {
    position: absolute;
    left: 43px;
    top: 231px;
    margin: 0;
    font-family: "Playfair Display", serif;
    font-style: italic;
    font-weight: 900;
    font-size: 29px;
    letter-spacing: -1.3px;
    line-height: 1;
    white-space: nowrap;
  }
  .address {
    position: absolute;
    left: 57px;
    top: 292px;
    margin: 0;
    font-family: "Archivo", sans-serif;
    font-weight: 800;
    font-size: 21px;
    line-height: 1;
    white-space: nowrap;
  }
  .contact-list {
    position: absolute;
    left: 57px;
    top: 408px;
    margin: 0;
    padding: 0;
    list-style: none;
    font-family: "Archivo", sans-serif;
    font-weight: 800;
    font-size: 21px;
    line-height: 1;
  }
  .contact-item {
    position: relative;
    height: 52.5px;
    white-space: nowrap;
  }
  .contact-label { position: absolute; left: 0; }
  .contact-value { position: absolute; left: 108px; }
  .contact-value.wide { left: 120px; }
</style>
</head>
<body>
  <main class="card">
    <div class="brand-mark" aria-hidden="true"></div>
    <h1 class="company-name">Varn Hydraulic &amp; Groundworks</h1>
    <p class="tagline">invite us to your next break down</p>

    <p class="person-name">Delia Pranton</p>
    <p class="person-title">Parts Manager</p>

    <p class="services">New &amp; used parts to suit all types of machinery service-repairs- overhauls- labour hire</p>
    <p class="address">Address : 2a Tembley Street (PO Box 6475) Mount Isa QLD 4825</p>

    <ul class="contact-list">
      <li class="contact-item"><span class="contact-label">Tel :</span><span class="contact-value">(07) 4916 2087</span></li>
      <li class="contact-item"><span class="contact-label">Fax:</span><span class="contact-value">(07) 4916 3650</span></li>
      <li class="contact-item"><span class="contact-label">Mobile:</span><span class="contact-value">(07) 4916 2087</span></li>
      <li class="contact-item"><span class="contact-label">Email :</span><span class="contact-value wide">parts@varnhydro.com.au</span></li>
      <li class="contact-item"><span class="contact-label">Web &nbsp;&nbsp;:</span><span class="contact-value wide">www.varnhydro.com.au</span></li>
    </ul>
  </main>
</body>
</html>
```